Quiet Meadow Counseling business cards

Dana Korvath, LCPC, NCC
(555)347-0618
www.quietmeadowcounseling.example
dana@quietmeadowcounseling.example

Business cards. I would like it on the same background as pictured. Not on a white business card. I have attached the logo that was done by another designer with artbazaar. I am open to looking at single-sided and double-sided designs.

Target Market(s)

teenagers and adults

Industry/Entity Type

mental health

Contact Information for Business Card

Dana Korvath, LCPC, NCC (555)347-0618 dana@quietmeadowcounseling.example

Font styles to use
Other font styles liked:
• Cinzel

Colors

Designer to choose colors to be used in the design.

Requirements
Must have
• logo that is attached

```html
<!DOCTYPE html>
<html lang="en">
<head>
<meta charset="UTF-8">
<title>Quiet Meadow Counseling – Business Cards</title>
<link rel="stylesheet" href="https://fonts.googleapis.com/css2?family=Montserrat:wght@400;500;700&display=swap">
<style>
  :root {
    --stage: #2a2c2f;
    --card-deep: #1f2c36;
    --card-mid: #33434f;
    --card-light: #4a5a66;
    --text-white: #ffffff;
    --text-soft: #c9d2d8;
    --brand: #a9c3cf;
    --rule: #8fa4ae;
  }
  * { margin: 0; padding: 0; box-sizing: border-box; }
  html, body { width: 1200px; height: 904px; overflow: hidden; }
  body {
    background: var(--stage);
    font-family: "Montserrat", sans-serif;
    position: relative;
  }
  .card {
    position: absolute;
    width: 640px;
    height: 366px;
    border-radius: 4px;
    overflow: hidden;
    box-shadow: 0 18px 40px rgba(0,0,0,0.45);
  }
  .card--front { left: 110px; top: 70px; }
  .card--back { left: 450px; top: 468px; }
  .card__backdrop {
    position: absolute; inset: 0;
    background:
      radial-gradient(ellipse at 30% 30%, var(--card-light) 0%, transparent 55%),
      radial-gradient(ellipse at 80% 70%, #3b4a55 0%, transparent 50%),
      linear-gradient(160deg, var(--card-mid) 0%, var(--card-deep) 100%);
  }
  .brand {
    position: absolute;
    left: 50%;
    transform: translateX(-50%);
    display: flex;
    flex-direction: column;
    align-items: center;
    gap: 10px;
  }
  .card--front .brand { top: 58px; }
  .card--back .brand { top: 92px; }
  .brand__dot {
    width: 64px; height: 64px;
    border-radius: 50%;
    background: var(--brand);
    opacity: 0.85;
  }
  .brand__name {
    font-weight: 700;
    font-size: 24px;
    letter-spacing: 0.06em;
    text-transform: uppercase;
    color: var(--brand);
    text-align: center;
    line-height: 1.25;
    white-space: nowrap;
  }
  .holder {
    position: absolute;
    left: 42px;
    bottom: 48px;
  }
  .holder__name {
    font-weight: 700;
    font-size: 27px;
    color: var(--text-white);
  }
  .holder__creds {
    margin-top: 8px;
    font-size: 14px;
    color: var(--text-soft);
    letter-spacing: 0.04em;
  }
  .contact {
    position: absolute;
    right: 28px;
    bottom: 56px;
    list-style: none;
    display: flex;
    flex-direction: column;
    gap: 9px;
  }
  .contact__item {
    display: flex;
    align-items: center;
    gap: 9px;
    font-size: 14px;
    color: var(--text-white);
  }
  .contact__item svg { width: 14px; height: 14px; flex: none; }
  .contact__item--web { padding-left: 23px; }
</style>
</head>
<body>

  <section class="card card--front">
    <div class="card__backdrop" role="img" aria-label="Softly blurred photo of a calm counseling office interior in slate blue tones"></div>
    <div class="brand">
      <span class="brand__dot"></span>
      <span class="brand__name">Quiet Meadow<br>Counseling</span>
    </div>
    <div class="holder">
      <p class="holder__name">Dana Korvath</p>
      <p class="holder__creds">LCPC, NCC</p>
    </div>
    <ul class="contact">
      <li class="contact__item contact__item--web">www.quietmeadowcounseling.example</li>
      <li class="contact__item">
        <svg viewBox="0 0 16 16" aria-hidden="true"><path fill="#ffffff" d="M3.6 1.5l2.3 2.6-1.3 1.7a9 9 0 0 0 5.6 5.6l1.7-1.3 2.6 2.3-1.6 2.1C7.3 14 2 8.7 1.5 3.1z"/></svg>
        (555)347-0618
      </li>
      <li class="contact__item">
        <svg viewBox="0 0 16 16" aria-hidden="true"><rect x="1" y="3" width="14" height="10" fill="#ffffff"/><path d="M1 3l7 6 7-6" fill="none" stroke="#1f2c36" stroke-width="1.2"/></svg>
        dana@quietmeadowcounseling.example
      </li>
    </ul>
  </section>

  <section class="card card--back">
    <div class="card__backdrop" role="img" aria-label="Softly blurred photo of a calm counseling office interior in slate blue tones"></div>
    <div class="brand">
      <span class="brand__dot"></span>
      <span class="brand__name">Quiet Meadow<br>Counseling</span>
    </div>
  </section>

</body>
</html>
```